Project Transparent, Clean, and Simple.

Please use the current website for any materials: www.veltrosimard.com - I don't have anything that I can upload - sorry :)

To clarify we want to create pages for each tab on the existing site. If you think there is a better way to group these or showcase these categories please feel free to do so but please include these pages.

1.Home Page
Your Needs should each have a separate page
2. Family Office
3. Entrepreneurs
4.Clear Steward
5. Your Team
6. Insights
7. News & Media
8. Contact Us

We just want this site to look like Quorva.com. Simple. Easy. Impactful.
Current website again is:
https://www.veltrosimard.com/

We are doing something completely different from everyone else in our industry, and we want people to realize that this is not an ordinary place. We want to bring transparency to our clients, make them feel comfortable and gain trust in our beliefs. We provide everything from doing your taxes, travel planning, financial planning, estate planning, legal work, family and life management issues - etc. Our main service is managing money but with the obligation of providing our clients options that have their best interests in mind - which most banks cannot and do not do.

If our site does not show that we are simple, transparent, and easy to use. We won't be able to get that far. It also needs to be easy enough to view videos and for people to sign up to learn more without being in front of your face as the main call to action.

Target Market(s)

Entrepreneurs and High Net Worth Individuals

Industry/Entity Type

Financial Service

Number of Pages Required

5+ page

Font styles to use
Sans Serif
Other font styles liked:
• Times New Roman, Palatino, Georgia, Courier, Bookman and Garamond

Colors
1b1b1b
ffffff
0292cd

Requirements
Must have
• Simple. A lot of White Space. Needs to look as simple and impactful as Quorva.com.
Nice to have
• White Space
Should not have
• A lot of colors. Not much White Space. Busy.

```html
<!DOCTYPE html>
<html lang="en">
<head>
<meta charset="utf-8">
<title>Veltrosimard — Transparent Family Wealth Advisors</title>
<link rel="stylesheet" href="https://fonts.googleapis.com/css2?family=Noto+Serif:wght@400;700&family=Source+Serif+4:wght@400;600&display=swap">
<style>
:root{
  --ink:#1b1b1b;
  --white:#ffffff;
  --blue:#0553a8;
  --card:#f3f3f3;
  --card-alt:#f7f7f7;
  --muted:#8a8a8a;
  --rule:#dcdcdc;
  --dark:#141414;
}
*{box-sizing:border-box;margin:0;padding:0}
html,body{width:1188px;height:1200px;overflow:hidden;background:var(--white)}
body{position:relative;font-family:"Noto Serif",Georgia,serif;color:var(--ink)}
.hero{position:absolute;left:0;top:0;width:1188px;height:603px;
  background:radial-gradient(ellipse at 58% 40%,#4a4a4a 0%,#2a2a2a 35%,#161616 75%,#0e0e0e 100%)}
.brand{position:absolute;display:flex;flex-direction:column;color:var(--white)}
.brand-name{font-family:"Source Serif 4",Georgia,serif;font-weight:600;font-size:23px;line-height:1}
.brand-tag{font-size:10.5px;margin-top:4px;color:var(--white);font-family:"Noto Serif",Georgia,serif}
.site-header .brand{left:198px;top:20px}
.main-nav{position:absolute;left:468px;top:25px;display:flex;align-items:center;font-size:10.5px;color:var(--white)}
.main-nav a{color:inherit;text-decoration:none;padding:8px 10px;position:relative}
.main-nav a.active::after{content:"";position:absolute;left:4px;right:4px;bottom:-5px;height:2px;background:var(--white)}
.main-nav .cta{border:1px solid var(--white);margin-left:6px;padding:7px 10px}
.slider-arrow{position:absolute;top:292px}
.slider-arrow.prev{left:62px}.slider-arrow.next{left:1106px}
.hero-title{position:absolute;left:0;width:1188px;top:330px;text-align:center;color:var(--white);
  font-family:"Source Serif 4",Georgia,serif;font-weight:400;font-size:35px;letter-spacing:.3px}
.services{position:absolute;top:603px;left:0;width:1188px;height:185px;display:flex;border-bottom:1px solid var(--rule)}
.service{width:297px;height:100%;padding:0 18px;background:var(--card);position:relative}
.service:nth-child(3){background:var(--card-alt)}
.service.featured{background:var(--blue);color:var(--white)}
.service-head{display:flex;align-items:center;gap:8px;height:112px}
.service-head h2{font-family:"Source Serif 4",Georgia,serif;font-weight:400;font-size:19px}
.service p{font-size:10px;line-height:18px;color:var(--muted);margin-top:-4px}
.service.featured p{color:var(--white)}
.press{position:absolute;top:788px;left:0;width:1188px;height:115px;display:flex;align-items:center;justify-content:space-between;padding:0 52px;border-bottom:1px solid var(--rule)}
.press span{font-family:"Source Serif 4",Georgia,serif;font-weight:600;font-size:16px;color:#2a2a2a}
.site-footer{position:absolute;top:903px;left:0;width:1188px;height:230px}
.footer-col{position:absolute;top:35px}
.footer-col h3{font-size:10.5px;font-weight:400;color:var(--ink);margin-bottom:30px}
.footer-col li{list-style:none;font-size:10px;color:var(--muted);height:22px}
.bottom-bar{position:absolute;top:1133px;left:0;width:1188px;height:67px;background:var(--dark);color:var(--white)}
.bottom-bar .brand{left:187px;top:15px}
.copyright{position:absolute;left:648px;top:27px;font-size:10.5px}
.version{position:absolute;left:1148px;top:27px;font-size:10.5px;color:#bbb}
</style>
</head>
<body>
<header class="site-header">
  <div class="hero" role="img" aria-label="Black and white photograph of a raised fist above a crowd"></div>
  <div class="brand">
    <div class="brand-name">Veltrosimard</div>
    <div class="brand-tag">Transparent Family Wealth Advisors</div>
  </div>
  <nav class="main-nav">
    <a class="active">Home</a><a>Your Needs</a><a>Your Team</a><a>Insights</a><a>News and Media</a><a>Contact Us</a><a class="cta">Get Started Today !</a>
  </nav>
  <svg class="slider-arrow prev" width="20" height="48" viewBox="0 0 20 48" fill="#fff"><circle cx="15" cy="3" r="1.7"/><circle cx="10" cy="12" r="1.7"/><circle cx="4" cy="23" r="1.7"/><circle cx="10" cy="34" r="1.7"/><circle cx="15" cy="44" r="1.7"/></svg>
  <svg class="slider-arrow next" width="20" height="48" viewBox="0 0 20 48" fill="#fff"><circle cx="5" cy="3" r="1.7"/><circle cx="10" cy="12" r="1.7"/><circle cx="16" cy="23" r="1.7"/><circle cx="10" cy="34" r="1.7"/><circle cx="5" cy="44" r="1.7"/></svg>
  <h1 class="hero-title">Transparent Family Wealth Advisors</h1>
</header>

<section class="services">
  <article class="service featured">
    <div class="service-head">
      <svg width="32" height="42" viewBox="0 0 32 42" fill="none" stroke="#fff" stroke-width="1.6"><rect x="2" y="2" width="28" height="38" rx="3"/><rect x="6" y="6" width="20" height="7"/><path d="M6 17h20v19H6zM11 17v19M16 17v19M21 17v19M6 22h20M6 27h20M6 32h20"/></svg>
      <h2>Taxes</h2>
    </div>
    <p>Neque porro quisquam est qui dolorem ipsum quia dolor sit amet, consectetur, adipisci velit...</p>
  </article>
  <article class="service">
    <div class="service-head">
      <svg width="50" height="34" viewBox="0 0 50 34" fill="none" stroke="#0553a8" stroke-width="1.6"><path d="M1 32h48M2 32l16-18 7 7 6-6 17 17"/><path d="M18 14V2l9 3-9 4"/><path d="M10 24l5 2 4-3 5 3"/></svg>
      <h2>Travel Planning</h2>
    </div>
    <p>Neque porro quisquam est qui dolorem ipsum quia dolor sit amet, consectetur, adipisci velit...</p>
  </article>
  <article class="service">
    <div class="service-head">
      <svg width="44" height="42" viewBox="0 0 44 42" fill="none" stroke="#0553a8" stroke-width="1.6"><circle cx="26" cy="7" r="5"/><path d="M8 22c0-7 7-11 16-11s16 4 16 11-5 10-9 11v6h-5v-4h-6v4h-5v-6c-3-1-6-4-6-6H3v-8h5z"/><circle cx="32" cy="20" r="1"/></svg>
      <h2>Financial Planning</h2>
    </div>
    <p>Neque porro quisquam est qui dolorem ipsum quia dolor sit amet, consectetur, adipisci velit...</p>
  </article>
  <article class="service">
    <div class="service-head">
      <svg width="42" height="42" viewBox="0 0 42 42" fill="none" stroke="#0553a8" stroke-width="1.6"><path d="M10 2h22v14a11 11 0 0 1-22 0z"/><path d="M10 6H2c0 8 4 13 9 14M32 6h8c0 8-4 13-9 14M21 27v7M14 40h14l-2-6H16z"/><path d="M21 8l2 4 4 .5-3 3 .8 4-3.8-2-3.8 2 .8-4-3-3 4-.5z"/></svg>
      <h2>Estate Planning</h2>
    </div>
    <p>Neque porro quisquam est qui dolorem ipsum quia dolor sit amet, consectetur, adipisci velit...</p>
  </article>
</section>

<section class="press" aria-label="As seen in">
  <span>Northwire</span><span>Tallyview</span><span>KMX</span><span>Brightmark</span><span>QTN</span><span>Daily Atlas</span><span>Ledgerline</span><span>Capitolian</span><span>WDR</span><span>Pellam</span>
</section>

<footer class="site-footer">
  <div class="footer-col" style="left:185px">
    <h3>Quick Links</h3>
    <ul><li>Home</li><li>Your Needs</li><li>Your Team</li><li>Insights</li><li>News and Media</li><li>Contact Us</li></ul>
  </div>
  <div class="footer-col" style="left:386px">
    <h3>Contact Us</h3>
    <ul><li>4820 Harbor Crest Lane | Suite 310</li><li>Alderford, VA 20455</li><li>Office: (555) 214-3800</li><li>Toll free: 855-01-CLEAR</li><li>info@veltrosimard.com</li></ul>
  </div>
  <div class="footer-col" style="left:635px">
    <h3>Your Needs</h3>
    <ul><li>Family Office</li><li>American Entrepreneurs</li><li>Clear Steward™</li></ul>
  </div>
  <div class="footer-col" style="left:833px">
    <h3>News &amp; Media</h3>
    <ul><li>Press Coverage</li><li>About the Expert</li><li>Press Releases</li><li>Videos</li><li>Contact Us</li></ul>
  </div>
</footer>

<div class="bottom-bar">
  <div class="brand">
    <div class="brand-name">Veltrosimard</div>
    <div class="brand-tag">Transparent Family Wealth Advisors</div>
  </div>
  <p class="copyright">© 2016 Veltrosimard | Ledgerline's Top 100 Financial Advisor and Family Office</p>
  <p class="version">C5</p>
</div>
</body>
</html>
```